K&R Security Services PTY. LTD.

Ive just had my logo made and I'm looking for some simple but strong designs for my business cards the company is a security company.

Please use dark colors.

Regards,

Owen Deloit

Reason: Need more time for discussion with other directors

Industry/Entity Type

Security

Font styles to use
Sans Serif
Decorative

```html
<!DOCTYPE html>
<html lang="en">
<head>
<meta charset="utf-8">
<title>K&amp;R Security Services – Business Card</title>
<link rel="stylesheet" href="https://fonts.googleapis.com/css2?family=Saira+Extra+Condensed:wght@600&family=Hind:wght@300;400&display=swap">
<style>
  :root {
    --page: #ffffff;
    --card: #0b0b0b;
    --ink-light: #ffffff;
    --ink-grey: #a9a9a9;
    --rule-grey: #9a9a9a;
    --mark-grey: #8c8c8c;
    --mark-faint: #1c1c1c;
  }
  * { margin: 0; padding: 0; box-sizing: border-box; }
  html, body {
    width: 1200px; height: 1000px; overflow: hidden;
    background: var(--page);
  }
  .canvas { position: relative; width: 1200px; height: 1000px; }

  .card { position: absolute; background: var(--card); overflow: hidden; }
  .card--front { left: 267px; top: 65px; width: 691px; height: 415px; }
  .card--back  { left: 264px; top: 522px; width: 694px; height: 417px; }

  .brand {
    position: absolute; display: flex; align-items: center; gap: 12px;
    font-family: "Saira Extra Condensed", sans-serif; font-weight: 600;
    letter-spacing: 2px; color: var(--mark-grey); white-space: nowrap;
  }
  .brand__dot { border-radius: 50%; background: var(--mark-grey); flex: none; }
  .brand--front { left: 50%; top: 50%; transform: translate(-50%, -50%); font-size: 58px; }
  .brand--front .brand__dot { width: 22px; height: 22px; }
  .brand--back { left: 486px; top: 216px; transform: translateX(-50%); font-size: 28px; }
  .brand--back .brand__dot { width: 12px; height: 12px; }

  .holder { position: absolute; left: 45px; top: 56px; }
  .holder__rule { display: flex; height: 3px; width: 195px; }
  .holder__rule span:first-child { width: 112px; background: var(--rule-grey); }
  .holder__rule span:last-child { flex: 1; background: var(--ink-light); }
  .holder__name {
    margin-top: 4px;
    font-family: "Saira Extra Condensed", sans-serif; font-weight: 600;
    font-size: 42px; line-height: 1; letter-spacing: 0.5px;
    color: var(--ink-light); text-transform: uppercase;
  }

  .contact {
    position: absolute; left: 52px; top: 222px; list-style: none;
    font-family: "Hind", sans-serif; font-weight: 300;
    font-size: 23px; line-height: 26px; color: var(--ink-grey);
  }
  .contact__item { display: flex; align-items: flex-start; gap: 8px; margin-bottom: 8px; }
  .contact__icon { width: 20px; height: 20px; flex: none; margin-top: 2px; fill: var(--ink-light); }
</style>
</head>
<body>
<div class="canvas">

  <section class="card card--front">
    <div class="brand brand--front"><span class="brand__dot"></span>K&amp;R SECURITY</div>
  </section>

  <section class="card card--back">
    <div class="holder">
      <div class="holder__rule"><span></span><span></span></div>
      <h1 class="holder__name">Owen Deloit</h1>
    </div>

    <div class="brand brand--back"><span class="brand__dot"></span>K&amp;R SECURITY</div>

    <ul class="contact">
      <li class="contact__item">
        <svg class="contact__icon" viewBox="0 0 24 24" aria-hidden="true"><path d="M6.6 10.8a15.1 15.1 0 0 0 6.6 6.6l2.2-2.2a1 1 0 0 1 1-.25 11.4 11.4 0 0 0 3.6.57 1 1 0 0 1 1 1V20a1 1 0 0 1-1 1A17 17 0 0 1 3 4a1 1 0 0 1 1-1h3.5a1 1 0 0 1 1 1c0 1.25.2 2.45.57 3.57a1 1 0 0 1-.25 1z"/></svg>
        <span>(03)9.555.0147</span>
      </li>
      <li class="contact__item">
        <svg class="contact__icon" viewBox="0 0 24 24" aria-hidden="true"><path d="M2 5h20v14H2z M2 5l10 8 10-8" /><path d="M2 6.5l10 7.5 10-7.5V5H2z" fill="#0b0b0b"/></svg>
        <span>k.r@krsecure.net.com<br>owen@krsecure.net.com</span>
      </li>
      <li class="contact__item">
        <svg class="contact__icon" viewBox="0 0 24 24" aria-hidden="true"><path d="M12 2a7 7 0 0 0-7 7c0 5.2 7 13 7 13s7-7.8 7-13a7 7 0 0 0-7-7zm0 9.5A2.5 2.5 0 1 1 12 6.5a2.5 2.5 0 0 1 0 5z"/></svg>
        <span>P.O.Box 7<br>Elmwood Victoria 3100</span>
      </li>
    </ul>
  </section>

</div>
</body>
</html>
```